Email signature banner for companys 60th anniversary

We are a transportation company. This is what our website people came up with so far:

https://www.plandeckly.com/design/7xQwPz2LmN4rTbVc8HyUoK/Movren?node-id=1830-12

I want a picture of our transport truck with the decal on the back that we are putting on it.

Our website is www.movren.com

Target Market(s)

Customer recognition

Industry/Entity Type

fuel and oil distribution company

Requirements
Must have
• our 60th anniversary logo
Nice to have
• Delivering Energy to Build Communites.
Should not have
• picture of the guy from the current banner provided

```html
<!DOCTYPE html>
<html lang="en">
<head>
<meta charset="utf-8">
<title>Movren 60th Anniversary Email Banners</title>
<link href="https://fonts.googleapis.com/css2?family=Bebas+Neue&display=swap" rel="stylesheet">
<style>
  :root {
    --navy: #1f3a73;
    --sky: #4f8ac9;
    --sky-light: #7fa9dd;
    --red: #d2242a;
    --white: #ffffff;
    --truck-grey: #c9ccd1;
  }
  html, body { margin: 0; padding: 0; overflow: hidden; }
  body {
    width: 1200px; height: 1200px;
    background: var(--white);
    position: relative;
    font-family: "Bebas Neue", "Arial Narrow", sans-serif;
  }
  .banner {
    position: absolute;
    left: 69px;
    width: 1070px;
    height: 268px;
    overflow: hidden;
  }
  .banner--navy { top: 311px; }
  .banner--sky { top: 649px; }
  .banner__bg { position: absolute; inset: 0; }
  .truck-art {
    position: absolute;
    left: 16px; top: 27px;
    width: 310px; height: 225px;
    border-radius: 10px;
  }
  .banner--navy .truck-art {
    background: radial-gradient(ellipse at 45% 45%, #e4e6ea 0%, var(--truck-grey) 40%, #4b5566 75%, rgba(31,58,115,0) 100%);
  }
  .banner--sky .truck-art {
    background: radial-gradient(ellipse at 45% 45%, #e4e6ea 0%, var(--truck-grey) 40%, #4b5566 75%, rgba(79,138,201,0) 100%);
  }
  .headline {
    position: absolute;
    left: 333px; top: 34px;
    margin: 0;
    font-weight: 400;
    line-height: 1;
    letter-spacing: 1px;
  }
  .headline__top { display: block; font-size: 81px; }
  .headline__bottom { display: block; font-size: 121px; margin-top: -6px; letter-spacing: 2px; }
  .banner--navy .headline { color: var(--white); }
  .banner--sky .headline { color: var(--navy); }
  .anniversary-mark {
    position: absolute;
    display: flex; flex-direction: column; align-items: center;
    color: var(--sky);
  }
  .banner--navy .anniversary-mark { left: 725px; top: 88px; width: 240px; }
  .banner--sky .anniversary-mark { left: 800px; top: 62px; width: 240px; }
  .anniversary-mark__name {
    display: flex; align-items: center; gap: 10px;
    font-size: 86px; line-height: 1; letter-spacing: 2px;
  }
  .anniversary-mark__dot {
    width: 22px; height: 22px; border-radius: 50%;
    background: var(--sky);
  }
  .anniversary-mark__est {
    margin-top: 14px;
    font-size: 19px; letter-spacing: 4px;
    color: var(--white);
  }
  .banner--sky .anniversary-mark__est { margin-top: 22px; }
</style>
</head>
<body>

<section class="banner banner--navy">
  <svg class="banner__bg" width="1070" height="268" viewBox="0 0 1070 268">
    <defs>
      <linearGradient id="stripeFadeNavy" x1="0" x2="1">
        <stop offset="0" stop-color="#4f8ac9"/>
        <stop offset="1" stop-color="#4f8ac9" stop-opacity="0"/>
      </linearGradient>
    </defs>
    <rect width="1070" height="268" fill="var(--red)"/>
    <path d="M0 0 H886 C930 48 1014 110 1014 183 C1014 220 992 248 969 268 H0 Z" fill="var(--navy)"/>
    <path d="M886 0 C930 48 1014 110 1014 183 C1014 220 992 248 969 268" fill="none" stroke="var(--sky)" stroke-width="4"/>
    <g fill="url(#stripeFadeNavy)">
      <rect x="0" y="14" width="440" height="8"/>
      <rect x="0" y="35" width="430" height="8"/>
      <rect x="0" y="56" width="300" height="8"/>
      <rect x="0" y="77" width="280" height="8"/>
      <rect x="0" y="98" width="260" height="8"/>
      <rect x="0" y="119" width="240" height="8"/>
      <rect x="0" y="140" width="220" height="8"/>
    </g>
  </svg>
  <div class="truck-art" role="img" aria-label="Illustration of a white fuel tanker truck seen from the rear, carrying the company anniversary decal"></div>
  <h1 class="headline">
    <span class="headline__top">Celebrating</span>
    <span class="headline__bottom">60 Years</span>
  </h1>
  <div class="anniversary-mark">
    <div class="anniversary-mark__name"><span class="anniversary-mark__dot"></span>Movren</div>
    <div class="anniversary-mark__est">Est. 1965</div>
  </div>
</section>

<section class="banner banner--sky">
  <svg class="banner__bg" width="1070" height="268" viewBox="0 0 1070 268">
    <defs>
      <linearGradient id="stripeFadeSky" x1="0" x2="1">
        <stop offset="0" stop-color="#8fb4e4"/>
        <stop offset="1" stop-color="#8fb4e4" stop-opacity="0"/>
      </linearGradient>
    </defs>
    <rect width="1070" height="268" fill="var(--red)"/>
    <path d="M0 0 H646 C690 48 774 110 774 188 C774 225 752 250 728 268 H0 Z" fill="var(--sky)"/>
    <path d="M646 0 C690 48 774 110 774 188 C774 225 752 250 728 268" fill="none" stroke="var(--navy)" stroke-width="4"/>
    <g fill="url(#stripeFadeSky)">
      <rect x="0" y="14" width="440" height="8"/>
      <rect x="0" y="35" width="430" height="8"/>
      <rect x="0" y="56" width="300" height="8"/>
      <rect x="0" y="77" width="280" height="8"/>
      <rect x="0" y="98" width="260" height="8"/>
      <rect x="0" y="119" width="240" height="8"/>
      <rect x="0" y="140" width="220" height="8"/>
    </g>
  </svg>
  <div class="truck-art" role="img" aria-label="Illustration of a white fuel tanker truck seen from the rear, carrying the company anniversary decal"></div>
  <h1 class="headline">
    <span class="headline__top">Celebrating</span>
    <span class="headline__bottom">60 Years</span>
  </h1>
  <div class="anniversary-mark">
    <div class="anniversary-mark__name"><span class="anniversary-mark__dot"></span>Movren</div>
    <div class="anniversary-mark__est">Est. 1965</div>
  </div>
</section>

</body>
</html>
```